Manufacturing company needs new business card.

I need a unique Business Card that will truly stand out. Nothing too busy. Simple is good, right? Not looking for a standard design either. No cookie cutter layout. I am just looking for something interesting and a bit different. Does't have to completely off the wall crazy, just not your run of the mill business card. Clean and modern with a touch of industrial.

Target Market(s)

Air conditioning industry, Architects, builders.

Industry/Entity Type

Business

Contact Information for Business Card

Details to be included on card are:

Peter Vance
Managing Director

T: 1300 847 519
M: 0428 593 174
W: www.brenvaleworks.com.au
E: peter.vance@brenvaleworks.com.au
A: 58 Harwick Lane, Sydney NSW 2000

Font styles to use
Sans Serif

Colors
0355a3
848484
fbfbfb

Requirements
Must have
• Card design must be landscape.

```html
<!DOCTYPE html>
<html lang="en">
<head>
<meta charset="utf-8">
<title>Brenvale Works — Business Card</title>
<link rel="stylesheet" href="https://fonts.googleapis.com/css2?family=Open+Sans:ital,wght@0,400;0,600;1,400&display=swap">
<style>
  :root {
    --brand-blue: #0355a3;
    --deep-blue: #1f4fb5;
    --steel-grey: #848484;
    --paper: #fbfbfb;
    --ink: #4a4a4a;
    --backdrop: #e4e6ea;
  }
  * { box-sizing: border-box; margin: 0; padding: 0; }
  html, body {
    width: 1200px; height: 800px; overflow: hidden;
    background: var(--backdrop);
    font-family: "Open Sans", Arial, sans-serif;
  }
  .canvas { position: relative; width: 1200px; height: 800px; }
  .card {
    position: absolute; top: 246px; width: 540px; height: 308px;
    overflow: hidden; box-shadow: 0 6px 18px rgba(0,0,0,.18);
  }
  .card--back { left: 40px; background: var(--deep-blue); }
  .card--front { left: 620px; background: var(--paper); }

  /* back */
  .back-brand {
    position: absolute; left: 0; right: 0; top: 94px;
    text-align: center;
    color: #fff; font-weight: 600; font-size: 36px; letter-spacing: .5px;
  }
  .back-band { position: absolute; left: 0; top: 214px; width: 196px; height: 14px; background: var(--steel-grey); }
  .back-web {
    position: absolute; left: 196px; top: 236px; width: 270px; height: 30px;
    background: #fff; display: flex; align-items: center; gap: 8px; padding-left: 14px;
    color: var(--brand-blue); font-size: 14px;
  }
  .back-tail { position: absolute; left: 480px; top: 250px; width: 60px; height: 14px; background: var(--steel-grey); }

  /* front */
  .front-brand {
    position: absolute; left: 28px; top: 22px;
    color: var(--brand-blue); font-weight: 600; font-size: 16px;
  }
  .person { position: absolute; left: 46px; top: 64px; }
  .person__name { color: var(--brand-blue); font-size: 23px; line-height: 1.1; }
  .person__title { color: var(--ink); font-style: italic; font-size: 13px; }
  .rule-blue { position: absolute; left: 0; top: 116px; width: 250px; height: 2px; background: var(--brand-blue); }
  .address { position: absolute; left: 28px; top: 128px; display: flex; gap: 10px; color: var(--ink); font-size: 13px; line-height: 1.35; }
  .bar-grey { position: absolute; left: 0; top: 176px; width: 190px; height: 12px; background: var(--steel-grey); }
  .rule-grey { position: absolute; left: 190px; top: 181px; width: 350px; height: 2px; background: var(--steel-grey); }
  .contacts { position: absolute; left: 200px; top: 194px; font-size: 14px; color: var(--ink); }
  .contact { display: flex; align-items: center; gap: 8px; height: 24px; }
  .contact--mobile { position: absolute; left: 150px; top: 0; white-space: nowrap; }
  .web-strip {
    position: absolute; left: 190px; top: 252px; width: 290px; height: 28px;
    background: var(--brand-blue); color: #fff; font-size: 14px;
    display: flex; align-items: center; gap: 8px; padding-left: 12px;
  }
  .tail-grey { position: absolute; left: 480px; top: 262px; width: 60px; height: 12px; background: var(--steel-grey); }
  .front-mark {
    position: absolute; right: 30px; top: 74px;
    color: var(--brand-blue); font-weight: 600; font-size: 24px;
  }
  svg { display: block; flex: none; }
</style>
</head>
<body>
<main class="canvas">

  <section class="card card--back" aria-label="Card back">
    <p class="back-brand">Brenvale Works</p>
    <div class="back-band"></div>
    <div class="back-web">
      <svg width="16" height="16" viewBox="0 0 16 16" fill="none" stroke="currentColor" stroke-width="1.3"><circle cx="8" cy="8" r="7"/><ellipse cx="8" cy="8" rx="3" ry="7"/><path d="M1 8h14M2.5 4.5h11M2.5 11.5h11"/></svg>
      <span>www.brenvaleworks.com.au</span>
    </div>
    <div class="back-tail"></div>
  </section>

  <section class="card card--front" aria-label="Card front">
    <p class="front-brand">Brenvale Works</p>
    <div class="person">
      <p class="person__name">Peter Vance</p>
      <p class="person__title">Managing Director</p>
    </div>
    <div class="rule-blue"></div>
    <div class="address">
      <svg width="14" height="20" viewBox="0 0 14 20" fill="var(--brand-blue)"><path d="M7 0a7 7 0 0 0-7 7c0 5 7 13 7 13s7-8 7-13a7 7 0 0 0-7-7zm0 10a3 3 0 1 1 0-6 3 3 0 0 1 0 6z"/></svg>
      <p>58 Harwick Lane,<br>Sydney NSW 2000</p>
    </div>
    <div class="bar-grey"></div>
    <div class="rule-grey"></div>
    <p class="front-mark">Brenvale Works</p>
    <div class="contacts">
      <div class="contact">
        <svg width="14" height="14" viewBox="0 0 24 24" fill="var(--brand-blue)"><path d="M6.6 10.8a15 15 0 0 0 6.6 6.6l2.2-2.2c.3-.3.7-.4 1-.2 1.1.4 2.3.6 3.6.6.6 0 1 .4 1 1V20c0 .6-.4 1-1 1A17 17 0 0 1 3 4c0-.6.4-1 1-1h3.5c.6 0 1 .4 1 1 0 1.3.2 2.5.6 3.6.1.3 0 .7-.2 1z"/></svg>
        <span>1300 847 519</span>
      </div>
      <div class="contact contact--mobile">
        <svg width="12" height="18" viewBox="0 0 12 18" fill="none" stroke="var(--brand-blue)" stroke-width="1.5"><rect x="1" y="1" width="10" height="16" rx="2"/><path d="M5 14.5h2"/></svg>
        <span>0428 593 174</span>
      </div>
      <div class="contact">
        <svg width="14" height="11" viewBox="0 0 14 11" fill="var(--brand-blue)"><path d="M0 0h14v11H0z"/><path d="M0 0l7 6 7-6" fill="none" stroke="#fff" stroke-width="1.2"/></svg>
        <span>peter.vance@brenvaleworks.com.au</span>
      </div>
    </div>
    <div class="web-strip">
      <svg width="16" height="16" viewBox="0 0 16 16" fill="none" stroke="currentColor" stroke-width="1.3"><circle cx="8" cy="8" r="7"/><ellipse cx="8" cy="8" rx="3" ry="7"/><path d="M1 8h14M2.5 4.5h11M2.5 11.5h11"/></svg>
      <span>www.brenvaleworks.com.au</span>
    </div>
    <div class="tail-grey"></div>
  </section>

</main>
</body>
</html>
```